Redesign Colorful Business Card

Please redesign the card attached. It is too busy. Please don't eliminate any of the words. The repetivite word "free" can be used less often.

Target Market(s)

College Students.

Contact Information for Business Card

The details listed in the attached image

Font styles to use
Sans Serif

Requirements
Must have
• A clear and simple presentation and must be attractive.

```html
<!DOCTYPE html>
<html lang="en">
<head>
<meta charset="UTF-8">
<title>StudyNimbl Business Card</title>
<link rel="stylesheet" href="https://fonts.googleapis.com/css2?family=Poppins:wght@600;700&display=swap">
<style>
  :root {
    --backdrop: #ececec;
    --card-bg: #222222;
    --circle: #ffffff;
    --red: #e8000b;
    --magenta: #e619e6;
    --teal: #1cc4c4;
    --ink: #111111;
    --brand-text: #ffffff;
  }
  * { margin: 0; padding: 0; box-sizing: border-box; }
  html, body {
    width: 1200px;
    height: 1200px;
    overflow: hidden;
    background: var(--backdrop);
  }
  .business-card {
    position: absolute;
    left: 75px;
    top: 300px;
    width: 1050px;
    height: 600px;
    background: var(--card-bg);
    overflow: hidden;
    border-radius: 6px;
    font-family: "Poppins", Arial, sans-serif;
  }
  .brand {
    position: absolute;
    left: 60px;
    top: 62px;
    display: flex;
    align-items: center;
    gap: 16px;
  }
  .brand-dot {
    width: 36px;
    height: 36px;
    border-radius: 50%;
    background: var(--magenta);
  }
  .brand-name {
    font-size: 40px;
    line-height: 1;
    font-weight: 600;
    color: var(--brand-text);
  }
  .free-badge {
    position: absolute;
    right: 60px;
    top: 40px;
    width: 96px;
    height: 96px;
    transform: rotate(-15deg);
  }
  .free-badge svg {
    position: absolute;
    inset: 0;
    width: 100%;
    height: 100%;
  }
  .free-badge .badge-label {
    position: absolute;
    inset: 0;
    display: flex;
    align-items: center;
    justify-content: center;
    font-size: 19px;
    font-weight: 700;
    color: var(--ink);
  }
  .promo-row {
    position: absolute;
    left: 30px;
    right: 30px;
    top: 220px;
    display: flex;
    justify-content: space-between;
  }
  .promo-circle {
    width: 310px;
    height: 310px;
    padding: 0 20px;
    border-radius: 50%;
    background: var(--circle);
    display: flex;
    align-items: center;
    justify-content: center;
    text-align: center;
    font-size: 26px;
    line-height: 1.2;
    font-weight: 700;
    text-transform: uppercase;
    white-space: nowrap;
  }
  .promo-memorize { color: var(--red); }
  .promo-study-time { color: var(--magenta); }
  .promo-no-class { color: var(--teal); }
</style>
</head>
<body>
  <main class="business-card">
    <div class="brand">
      <span class="brand-dot"></span>
      <span class="brand-name">StudyNimbl</span>
    </div>

    <div class="free-badge">
      <svg viewBox="0 0 100 100" aria-hidden="true">
        <polygon fill="var(--magenta)" points="100,50 88.6,60.4 93.3,75 78.3,78.3 75,93.3 60.4,88.6 50,100 39.6,88.6 25,93.3 21.7,78.3 6.7,75 11.4,60.4 0,50 11.4,39.6 6.7,25 21.7,21.7 25,6.7 39.6,11.4 50,0 60.4,11.4 75,6.7 78.3,21.7 93.3,25 88.6,39.6"/>
      </svg>
      <span class="badge-label">FREE</span>
    </div>

    <section class="promo-row">
      <div class="promo-circle promo-memorize">Memorize<br>anything<br>quickly</div>
      <div class="promo-circle promo-study-time">Cut study<br>time down by<br>up to 50%</div>
      <div class="promo-circle promo-no-class">Learn a<br>subject without<br>having to go<br>to class</div>
    </section>
  </main>
</body>
</html>
```